Landscape Supplier and Excavation company needing a website revamp.

We need a web design for our company based out of northern Virginia. We make and deliver topsoil, mulch, and compost. We are also an excavation company. We provide a wide variety of excavation services, from residential to large commercial projects. We specialize in land clearing and building site preparation. We would like a site that looks very professional and makes us look like a large company. We've been in business since 1994 and have never had a really nice website. Our current website it www.hollowbrookloam.com and www.rkqmo.com for references. I like the information on the pages but would like something more professional looking. Doesn't HAVE to be 4 different pages, but I would like a contact form, our services, and our products/ pricing listed. We are properly licensed and insured and would like this included somewhere on the site.

Target Market(s)

Landscapers, Home Owners, Commercial

Industry/Entity Type

Excavation and Landscape Products Supplier

Number of Pages Required

4 page

Colors

Designer to choose colors to be used in the design.

Requirements
Must have
• Professional Look and Feel

```html
<!DOCTYPE html>
<html lang="en">
<head>
<meta charset="utf-8">
<title>Hollowbrook Loam and Excavation</title>
<link href="https://fonts.googleapis.com/css2?family=Poppins:wght@400;500;600;700&display=swap" rel="stylesheet">
<style>
:root{
  --red:#c41f27;
  --ink:#222222;
  --text:#3a3a3a;
  --muted:#6b6b6b;
  --line:#dedede;
  --light:#f3f3f3;
  --dark:#1f2220;
  --white:#ffffff;
}
*{box-sizing:border-box;margin:0;padding:0}
html,body{width:1200px;height:4087px;overflow:hidden}
body{position:relative;font-family:"Poppins",sans-serif;color:var(--text);background:var(--white)}
.abs{position:absolute}
.red{color:var(--red)}
.section-title{position:absolute;left:0;width:1200px;text-align:center;font-size:36px;font-weight:600;color:var(--ink)}
.section-title span{font-weight:500;color:var(--red)}
.section-title::after{content:"";display:block;width:64px;height:2px;background:var(--red);margin:10px auto 0}
.section-title.on-dark{color:var(--white)}
.section-title.on-dark span{color:var(--white);font-weight:400}
.section-title.on-dark::after{display:none}

/* header */
.site-header{position:absolute;left:0;top:0;width:1200px;height:90px;background:var(--white);border-top:3px solid var(--red)}
.brand{position:absolute;left:162px;top:19px;width:246px;height:52px;border:2px solid var(--ink);display:flex;align-items:center;justify-content:center;gap:8px}
.brand-mark{width:12px;height:12px;background:var(--red)}
.brand-name{font-size:15px;font-weight:700;color:var(--red);letter-spacing:.3px}
.top-contact{position:absolute;top:12px;display:flex;align-items:center;gap:16px;font-size:15px;color:var(--ink)}
.icon-box{width:28px;height:28px;background:var(--red);display:flex;align-items:center;justify-content:center}
.main-nav{position:absolute;top:56px;left:592px;display:flex;gap:0;font-size:12.5px;color:var(--ink)}
.main-nav a{color:inherit;text-decoration:none;padding:4px 8px;margin-right:18px}
.main-nav a.active{border:1px solid var(--red);color:var(--red)}

/* hero */
.hero{position:absolute;left:0;top:90px;width:1200px;height:510px;background:linear-gradient(180deg,#6f8db2 0%,#9fb3c8 45%,#6d5b45 75%,#3f3326 100%)}
.hero-box{position:absolute;left:162px;top:209px;width:390px;height:254px;border:2px solid var(--white);padding:24px 14px}
.hero-small{font-size:30px;line-height:36px;color:var(--white)}
.hero-big{font-size:44px;line-height:50px;font-weight:700;color:var(--white);margin-top:8px}
.btn{display:inline-block;background:var(--red);color:var(--white);font-size:14px;font-weight:500;text-align:center}
.hero-btn{position:absolute;left:273px;top:444px;width:168px;height:34px;line-height:34px}
.slider-dots{position:absolute;left:1115px;top:310px}
.slider-dots i{display:block;width:12px;height:12px;background:#dcdcdc;margin-bottom:12px}
.slider-dots i.on{background:var(--red)}

/* about */
.about-title{position:absolute;left:162px;top:742px;font-size:36px;font-weight:600;color:var(--ink)}
.about-title span{font-weight:400;color:var(--red)}
.about-title::after{content:"";display:block;width:62px;height:2px;background:var(--red);margin-top:2px}
.about-lead{position:absolute;left:162px;top:818px;width:290px;font-size:15px;line-height:21px;color:var(--ink)}
.about-body{position:absolute;left:162px;top:872px;width:290px;font-size:13px;line-height:24px}
.about-body p{margin-bottom:12px}
.read-more{position:absolute;left:162px;top:1170px;width:111px;height:36px;line-height:36px}
.photo{position:absolute}
.framed{box-shadow:0 2px 10px rgba(0,0,0,.25)}
.years{position:absolute;left:492px;top:994px;width:262px;height:260px;border:6px solid #222;border-top-color:#555;background:#e8e8e8;text-align:center}
.years-num{font-size:128px;font-weight:700;color:#1d1d1d;line-height:150px;margin-top:10px;letter-spacing:-6px}
.years-label{font-size:28px;line-height:30px;color:var(--red);font-weight:500}

/* services */
.services{position:absolute;left:0;top:1330px;width:1200px;height:524px;background:linear-gradient(180deg,#232724,#2e332b 60%,#1c1f1c)}
.service-card{position:absolute;top:1479px;width:201px;height:299px;background:var(--white)}
.service-img{height:167px}
.service-label{height:28px;background:var(--red);color:var(--white);text-align:center;font-size:17px;line-height:28px;font-weight:500}
.service-text{padding:16px 14px 0;font-size:13px;line-height:21px;text-align:center;color:var(--ink)}
.plus{position:absolute;left:477px;top:1768px;width:20px;height:20px;border-radius:50%;background:var(--red);color:var(--white);font-size:16px;line-height:20px;text-align:center}

/* products */
.price-list{position:absolute;left:645px;top:2004px;width:395px;list-style:none}
.price-list li{height:39.5px;display:flex;align-items:center;justify-content:space-between;border-bottom:1px solid var(--line);font-size:13px;color:var(--ink)}
.price{width:66px;height:22px;border:1px solid var(--red);color:var(--red);font-size:13px;font-weight:600;text-align:center;line-height:20px;clip-path:polygon(8px 0,100% 0,100% 100%,8px 100%,0 50%)}
.price-note{position:absolute;left:250px;top:2430px;width:700px;text-align:center;font-size:16px;line-height:26px;color:var(--muted)}

/* gallery */
.gallery{position:absolute;left:0;top:2551px;width:1200px;height:604px;background:var(--light)}

/* contact */
.field{position:absolute;height:45px;border:1px solid var(--line);background:var(--white);display:flex;align-items:center;font-size:13px;color:var(--ink)}
.field .fi{width:46px;height:100%;background:#f2f2f2;border-right:1px solid var(--line);display:flex;align-items:center;justify-content:center}
.field span{padding-left:16px}
.field.area{align-items:flex-start}
.field.area span{padding-top:14px}
.submit{position:absolute;left:532px;top:3563px;width:135px;height:36px;line-height:36px}

/* footer */
.site-footer{position:absolute;left:0;top:3677px;width:1200px;height:367px;background:linear-gradient(180deg,#262826,#2d332c 60%,#1f231f);color:var(--white)}
.news-title{position:absolute;left:164px;top:68px;font-size:29px;font-weight:600}
.news-title span{font-weight:400}
.news-input{position:absolute;left:589px;top:71px;width:341px;height:43px;background:var(--white);color:#666;font-size:13px;line-height:43px;padding-left:16px}
.news-btn{position:absolute;left:930px;top:71px;width:106px;height:43px;line-height:43px;font-size:16px}
.footer-nav{position:absolute;top:187px;left:366px;display:flex;font-size:12.5px}
.footer-nav a{color:var(--white);text-decoration:none;margin-right:40px}
.footer-rule{position:absolute;left:0;top:170px;width:1200px;height:1px;background:rgba(255,255,255,.15)}
.footer-info{position:absolute;top:266px;display:flex;gap:12px;font-size:13.5px;line-height:23px}
.copyright{position:absolute;left:0;top:4044px;width:1200px;height:43px;background:var(--red);color:var(--white);font-size:13px;line-height:43px;padding-left:163px}
.social{position:absolute;top:4052px;width:28px;height:28px;border-radius:50%;background:var(--white)}
</style>
</head>
<body>

<header class="site-header">
  <div class="brand"><span class="brand-mark"></span><span class="brand-name">HOLLOWBROOK LOAM</span></div>
  <div class="top-contact" style="left:667px">
    <span class="icon-box"><svg width="16" height="12" viewBox="0 0 16 12"><rect x="1" y="1" width="14" height="10" fill="none" stroke="#fff" stroke-width="1.4"/><path d="M1 1l7 6 7-6" fill="none" stroke="#fff" stroke-width="1.4"/></svg></span>
    info@rkqmo.com
  </div>
  <div class="top-contact" style="left:897px;font-weight:500">
    <span class="icon-box"><svg width="16" height="16" viewBox="0 0 24 24"><path d="M6.6 10.8a15 15 0 006.6 6.6l2.2-2.2a1 1 0 011-.25 11.4 11.4 0 003.6.6 1 1 0 011 1V20a1 1 0 01-1 1A17 17 0 013 4a1 1 0 011-1h3.5a1 1 0 011 1c0 1.25.2 2.45.57 3.57a1 1 0 01-.25 1z" fill="none" stroke="#fff" stroke-width="1.6"/></svg></span>
    555-018-2740
  </div>
  <nav class="main-nav">
    <a class="active">Home</a><a>About Us</a><a>Services</a><a>Products/Pricing</a><a>Contact Us</a>
  </nav>
</header>

<section class="hero" role="img" aria-label="Excavator digging topsoil at a work site under a cloudy sky">
</section>
<div class="hero-box">
  <div class="hero-small">Produce The Very Best<br>Quality Topsoil</div>
  <div class="hero-big">For The<br>Best Results!</div>
</div>
<a class="btn hero-btn">Contact Us Today</a>
<div class="slider-dots"><i></i><i class="on"></i><i></i></div>

<h2 class="about-title">About <span>Us</span></h2>
<p class="about-lead">Hollowbrook Loam has been providing quality topsoil and mulch <span class="red">since 1992.</span></p>
<div class="about-body">
  <p>Our emphasis is to produce the very best quality topsoil for the best results! Our topsoil and organics make quality ready-made soils and lawn amendments. We can custom blend any products which include leaf mulch and Larkmoor compost to make the perfect mixtures for your needs.</p>
  <p>Whether you are looking for a excavation contractor or simply interested in our products, get in touch today to bring your vision to life!</p>
</div>
<a class="btn read-more">Read More</a>
<div class="photo framed" style="left:492px;top:708px;width:262px;height:262px;background:linear-gradient(160deg,#8fb0d0,#8a7562 55%,#5a4632)" role="img" aria-label="Screening machine producing topsoil"></div>
<div class="photo framed" style="left:776px;top:675px;width:264px;height:372px;background:linear-gradient(180deg,#d9c7a8,#a9b6c2 40%,#c9a43a 60%,#8a7a5e)" role="img" aria-label="Yellow excavator in front of mountains"></div>
<div class="years">
  <div class="years-num">29</div>
  <div class="years-label">Years of<br>Experience</div>
</div>

<section class="services" role="img" aria-label="Dark forest clearing with heavy equipment in the background"></section>
<h2 class="section-title on-dark" style="top:1394px">Our <span>Services</span></h2>
<div class="service-card" style="left:162px">
  <div class="service-img" style="background:linear-gradient(180deg,#c9d3dc,#a5a092 60%,#6f6a5a)" role="img" aria-label="Excavator at a job site"></div>
  <div class="service-label">Excavation</div>
  <div class="service-text">We specialize in land clearing and building site preparation.</div>
</div>
<div class="service-card" style="left:385px">
  <div class="service-img" style="background:linear-gradient(180deg,#e6e6e6,#9a9a9a 55%,#2a2a2a)" role="img" aria-label="Large pile of screened topsoil"></div>
  <div class="service-label">Topsoil</div>
  <div class="service-text">We can custom blend any of our products.</div>
</div>
<div class="service-card" style="left:611px">
  <div class="service-img" style="background:linear-gradient(180deg,#b8b2a8,#6b5a45 55%,#c2552a)" role="img" aria-label="Land clearing with burning brush pile"></div>
  <div class="service-label">Clearing</div>
  <div class="service-text">Land clearing is the process of removing trees, stumps, brush, ect.</div>
</div>
<div class="service-card" style="left:836px">
  <div class="service-img" style="background:linear-gradient(180deg,#e2e6ea,#c9b59c 45%,#9a6c4e)" role="img" aria-label="Graded dirt field with grading machine"></div>
  <div class="service-label">Grading</div>
  <div class="service-text">prepare the ground for home extensions, and for purely aesthetic purposes</div>
</div>
<div class="plus">+</div>

<h2 class="section-title" style="top:1918px">Products <span>And Pricing</span></h2>
<div class="photo" style="left:162px;top:2012px;width:449px;height:369px;background:#fff;padding:8px;box-shadow:0 2px 10px rgba(0,0,0,.2)">
  <div style="width:100%;height:100%;background:linear-gradient(160deg,#7ca24c,#7a6a4d 50%,#5f8a3c)" role="img" aria-label="Skid steer spreading topsoil on a lawn"></div>
</div>
<ul class="price-list">
  <li>Unscreened Topsoil<span class="price">$10</span></li>
  <li>Shredded Topsoil<span class="price">$14</span></li>
  <li>Screened Topsoil<span class="price">$20</span></li>
  <li>Double Shredded Hardwood Mulch<span class="price">$15</span></li>
  <li>Brown Dyed Mulch<span class="price">$28</span></li>
  <li>Black Dyed Mulch<span class="price">$28</span></li>
  <li>Premium Leaf Compost<span class="price">$27</span></li>
  <li>Larkmoor Soil Builder<span class="price">$34</span></li>
  <li>Screened Topsoil &amp; ½ Leaf Mulch<span class="price">$27</span></li>
  <li>Screened Topsoil &amp; ½ Larkmoor<span class="price">$34</span></li>
</ul>
<p class="price-note">All prices are per cubic yard. Delivery is available at a reasonable rate. Minimum delivery on all products is 8 cubic yards.</p>

<section class="gallery"></section>
<h2 class="section-title" style="top:2614px">Our <span>Gallery</span></h2>
<div class="photo" style="left:162px;top:2695px;width:382px;height:386px;background:linear-gradient(180deg,#a9bfd6,#b59a73 50%,#8a6e4c)" role="img" aria-label="Loader and screener in a sandy yard"></div>
<div class="photo" style="left:552px;top:2695px;width:191px;height:190px;background:linear-gradient(180deg,#c8d2c4,#7a9a52 60%,#5a4a3a)" role="img" aria-label="Mini excavator digging on a lawn"></div>
<div class="photo" style="left:749px;top:2695px;width:289px;height:190px;background:linear-gradient(170deg,#8aaed2,#7a6653 60%,#5a4532)" role="img" aria-label="Screening machine throwing soil"></div>
<div class="photo" style="left:552px;top:2892px;width:288px;height:189px;background:linear-gradient(160deg,#5f7d3c,#c2652a 40%,#6e6a60)" role="img" aria-label="Orange excavator bucket on a muddy site"></div>
<div class="photo" style="left:848px;top:2892px;width:190px;height:189px;background:linear-gradient(180deg,#b7c9dc,#d7dde2 45%,#a25a3c)" role="img" aria-label="Graded red clay site near buildings"></div>

<h2 class="section-title" style="top:3220px">Contact <span>Us</span></h2>
<div class="field" style="left:244px;top:3304px;width:345px"><div class="fi"><svg width="16" height="16" viewBox="0 0 16 16"><circle cx="8" cy="5" r="3" fill="none" stroke="#aaa"/><path d="M2 15c0-3.5 2.7-5 6-5s6 1.5 6 5" fill="none" stroke="#aaa"/></svg></div><span>Your Name*</span></div>
<div class="field" style="left:608px;top:3304px;width:343px"><div class="fi"><svg width="16" height="12" viewBox="0 0 16 12"><rect x="1" y="1" width="14" height="10" fill="none" stroke="#aaa"/><path d="M1 1l7 6 7-6" fill="none" stroke="#aaa"/></svg></div><span>Email*</span></div>
<div class="field" style="left:244px;top:3366px;width:345px"><div class="fi"><svg width="15" height="15" viewBox="0 0 24 24"><path d="M6.6 10.8a15 15 0 006.6 6.6l2.2-2.2a1 1 0 011-.25 11.4 11.4 0 003.6.6 1 1 0 011 1V20a1 1 0 01-1 1A17 17 0 013 4a1 1 0 011-1h3.5a1 1 0 011 1c0 1.25.2 2.45.57 3.57a1 1 0 01-.25 1z" fill="none" stroke="#aaa" stroke-width="1.6"/></svg></div><span>Phone*</span></div>
<div class="field" style="left:608px;top:3366px;width:343px"><div class="fi"><svg width="16" height="16" viewBox="0 0 16 16"><rect x="1" y="3" width="11" height="11" fill="none" stroke="#aaa"/><path d="M6 10l1-3 7-6 1 1-7 7z" fill="none" stroke="#aaa"/></svg></div><span>Inquiry For*</span></div>
<div class="field area" style="left:244px;top:3431px;width:707px;height:110px"><div class="fi" style="align-items:flex-start;padding-top:14px"><svg width="14" height="14" viewBox="0 0 16 16"><circle cx="8" cy="8" r="7" fill="none" stroke="#aaa"/><text x="8" y="12" font-size="10" text-anchor="middle" fill="#aaa" font-family="sans-serif">?</text></svg></div><span>How can we help you?</span></div>
<a class="btn submit">Submit Now</a>

<footer class="site-footer" role="img" aria-label="Dark photo of screening equipment behind footer content">
  <h3 class="news-title">Newsletter <span>Subscription</span></h3>
  <svg class="abs" style="left:485px;top:102px" width="110" height="40" viewBox="0 0 110 40"><path d="M2 8c10 20 40 28 60 22s20-22 8-18-4 20 36 12" fill="none" stroke="#fff" stroke-width="1.2" stroke-dasharray="3 3"/></svg>
  <div class="news-input">Enter your Email</div>
  <a class="btn news-btn">Subscribe</a>
  <div class="footer-rule"></div>
  <nav class="footer-nav"><a>Home</a><a>About Us</a><a>Services</a><a>Products/Pricing</a><a>Contact Us</a></nav>
  <div class="footer-info" style="left:162px">
    <svg width="16" height="20" viewBox="0 0 16 20"><path d="M8 19s6-6.5 6-11A6 6 0 002 8c0 4.5 6 11 6 11z" fill="none" stroke="#fff" stroke-width="1.3"/><circle cx="8" cy="8" r="2" fill="none" stroke="#fff"/></svg>
    <div>Address :<br>4410 Fernhollow Road, Millbrae,<br>Virginia 20000, United States</div>
  </div>
  <div class="footer-info" style="left:572px">
    <svg width="18" height="18" viewBox="0 0 24 24"><path d="M6.6 10.8a15 15 0 006.6 6.6l2.2-2.2a1 1 0 011-.25 11.4 11.4 0 003.6.6 1 1 0 011 1V20a1 1 0 01-1 1A17 17 0 013 4a1 1 0 011-1h3.5a1 1 0 011 1c0 1.25.2 2.45.57 3.57a1 1 0 01-.25 1z" fill="none" stroke="#fff" stroke-width="1.5"/></svg>
    <div>Call :<br>555-018-2740</div>
  </div>
  <div class="footer-info" style="left:884px">
    <svg width="20" height="15" viewBox="0 0 16 12"><rect x="1" y="1" width="14" height="10" fill="none" stroke="#fff"/><path d="M1 1l7 6 7-6" fill="none" stroke="#fff"/></svg>
    <div>Email :<br>info@rkqmo.com</div>
  </div>
</footer>
<div class="copyright">Copyright © 2021 Hollowbrook Loam - All Rights Reserved.</div>
<span class="social" style="left:966px"></span>
<span class="social" style="left:1009px"></span>

</body>
</html>
```